Corndell website

Provide a website for a business that is an online farmstand for mostly organic farm products produced on our 9 farms and packaged at our mill. We will be targeting an urban and suburban audience that will be able know the farms where their food is grown and "pick" their food online. We want the site to feel to feel fresh and urbane. Winning logo attached.

The website will feature:

A section with descriptions, pictures and Google maps for the farms as well as the produce produced on each farm. We will want to establish a provenance to the mostly organic food we produce and sell - and visit the farms if they want. We want our customers to know where their food comes from without having to live on a farm. We will market products of local farmers in addition to our own. We'll need room for about 50 farm descriptions and about 5 product descriptions per farm.

A master growing schedule -- there should be room for about 5 products per farm.

An online store (maybe linked to the farm and product) descriptions

An about us section -- where we can tell our family's story and about the history of the mill where we package food and provide fulfillment

A section for links to other farming and food information

A section for legal notices
Updates

Project Deadline Extended
Reason: Holiday weekend for many in USA

Target Market(s)

Educated, urban market who wants quality food at fair prices.

Industry/Entity Type

Farm

```html
<!DOCTYPE html>
<html lang="en">
<head>
<meta charset="utf-8">
<title>Corndell – Online Farmstand</title>
<link rel="stylesheet" href="https://fonts.googleapis.com/css2?family=Open+Sans:ital,wght@0,400;0,600;0,700;1,600&display=swap">
<style>
  :root {
    --header-green: #b5cb74;
    --olive: #5b7a1c;
    --olive-dark: #3f5a10;
    --ink: #2b2b2b;
    --text: #333333;
    --brown: #98560a;
    --page-grey: #e8e6e6;
    --white: #ffffff;
    --panel: rgba(40, 48, 28, 0.82);
    --icon-dark: #333a26;
  }
  * { box-sizing: border-box; margin: 0; padding: 0; }
  html, body { width: 911px; height: 1200px; overflow: hidden; }
  body {
    position: relative;
    font-family: "Open Sans", Arial, sans-serif;
    color: var(--text);
    background: var(--page-grey);
  }

  /* Header */
  .site-header {
    position: absolute; left: 0; top: 0; width: 911px; height: 78px;
    background: var(--header-green);
  }
  .brand {
    position: absolute; left: 119px; top: 48px;
    font-size: 20px; font-weight: 700; letter-spacing: 1.5px; color: var(--ink);
  }
  .utility-links {
    position: absolute; right: 146px; top: 18px;
    font-size: 9.5px; color: var(--ink);
    display: flex; gap: 8px; align-items: center;
  }
  .utility-links .login { display: flex; align-items: center; gap: 4px; }
  .main-nav {
    position: absolute; right: 146px; top: 49px;
    display: flex; gap: 23px;
    font-size: 9.5px; font-weight: 700; letter-spacing: 0.4px; text-transform: uppercase;
    color: var(--white);
  }
  .main-nav .current { color: var(--ink); }

  /* Hero */
  .hero-photo {
    position: absolute; left: 0; top: 78px; width: 911px; height: 225px;
    background: linear-gradient(180deg, #d9d2be 0%, #c4b79a 35%, #7d6a44 62%, #5a5a2a 80%, #8a7a3e 100%);
  }
  .farm-search {
    position: absolute; left: 118px; top: 106px; width: 260px; height: 170px;
    background: var(--panel);
  }
  .farm-search h2 {
    position: absolute; left: 23px; top: 18px;
    font-size: 11px; font-weight: 400; color: #c7dc8a;
  }
  .field {
    position: absolute; left: 21px; width: 203px; height: 30px;
    background: var(--white); border-radius: 15px;
    font-size: 9.5px; color: var(--ink);
    padding: 0 15px; display: flex; align-items: center; justify-content: space-between;
  }
  .field.location { top: 44px; }
  .field.food { top: 80px; }
  .go-button {
    position: absolute; left: 21px; top: 118px; width: 62px; height: 30px;
    background: var(--olive); border-radius: 15px;
    color: var(--white); font-size: 10px; font-weight: 600;
    display: flex; align-items: center; justify-content: center;
  }

  /* Map */
  .farm-map {
    position: absolute; left: 0; top: 303px; width: 911px; height: 209px;
    background: linear-gradient(90deg, #ecebe6 0%, #e6e4dc 38%, #a8c8ef 45%, #e6e4dc 52%, #ecebe6 100%);
  }

  /* Farm cards */
  .farm-card {
    position: absolute; left: 119px; width: 667px; height: 165px;
    background: var(--white);
    box-shadow: 0 1px 3px rgba(0,0,0,0.25);
  }
  .farm-card.first { top: 550px; }
  .farm-card.second { top: 734px; }
  .card-bar {
    height: 41px; background: var(--brown); color: var(--white);
    display: flex; align-items: center; justify-content: space-between;
    padding: 0 23px 0 15px; font-size: 12.5px;
  }
  .card-photo {
    position: absolute; left: 0; top: 41px; width: 182px; height: 124px;
  }
  .card-photo.market { background: linear-gradient(135deg, #c9b27a 0%, #e0b04a 45%, #9c6a3a 100%); }
  .card-photo.produce { background: radial-gradient(circle at 50% 55%, #8aa23c 0%, #c98c4a 40%, #f0eeea 80%); }
  .card-body {
    position: absolute; left: 203px; top: 51px; width: 440px;
  }
  .card-body h3 {
    font-size: 12.5px; font-weight: 400; color: var(--olive);
    margin-bottom: 3px;
  }
  .card-body p {
    font-size: 8.5px; line-height: 13px; color: var(--text);
    margin-bottom: 9px;
  }

  .more-link {
    position: absolute; left: 0; top: 923px; width: 905px;
    text-align: center; font-size: 9.5px; font-weight: 600; color: #555;
  }
  .more-link svg { display: block; margin: 1px auto 0; }

  /* Welcome */
  .welcome {
    position: absolute; left: 0; top: 965px; width: 911px; height: 172px;
    background: var(--white);
  }
  .welcome-title {
    position: absolute; left: 155px; top: 26px; width: 590px;
    display: flex; align-items: center; gap: 12px;
    font-size: 20px; font-weight: 400; color: var(--ink); white-space: nowrap;
  }
  .welcome-title .accent { color: var(--olive-dark); }
  .welcome-title .rule { flex: 1; border-top: 1px dotted #9a9a9a; }
  .welcome p {
    position: absolute; left: 187px; top: 64px; width: 533px;
    text-align: center; font-size: 8.5px; line-height: 12.5px; color: var(--text);
  }
  .welcome .read-more {
    position: absolute; left: 0; top: 114px; width: 907px;
    text-align: center; font-size: 10px; font-weight: 600; font-style: italic; color: var(--brown);
  }

  /* Footer */
  .site-footer {
    position: absolute; left: 0; top: 1137px; width: 911px; height: 63px;
    background: var(--header-green);
  }
  .site-footer .legal {
    position: absolute; left: 119px; top: 26px;
    font-size: 8.5px; color: var(--ink);
  }
  .social {
    position: absolute; left: 713px; top: 21px; display: flex; gap: 6px;
  }
  .social span {
    width: 20px; height: 20px; border-radius: 50%; background: var(--icon-dark); display: block;
  }
</style>
</head>
<body>

<header class="site-header">
  <div class="brand">CORNDELL</div>
  <div class="utility-links">
    <span>Farming and food information</span><span>|</span>
    <span>Legal Notice</span><span>|</span>
    <span class="login">
      <svg width="12" height="12" viewBox="0 0 12 12" aria-hidden="true">
        <circle cx="6" cy="3.5" r="2.8" fill="#3b4a22"/>
        <path d="M1 12 C1 7.5 11 7.5 11 12 Z" fill="#3b4a22"/>
      </svg>Login
    </span>
  </div>
  <nav class="main-nav">
    <span class="current">Home</span>
    <span>About Us</span>
    <span>Growing Schedule</span>
    <span>Store</span>
    <span>Contact Us</span>
  </nav>
</header>

<div class="hero-photo" role="img" aria-label="Photo of a wooden windmill and barn in farmland at sunset"></div>

<section class="farm-search">
  <h2>Search Your Farm</h2>
  <div class="field location">Location
    <svg width="8" height="6" viewBox="0 0 8 6" aria-hidden="true"><path d="M0 0 H8 L4 6 Z" fill="#333"/></svg>
  </div>
  <div class="field food">Food</div>
  <div class="go-button">Go</div>
</section>

<div class="farm-map" role="img" aria-label="Street map with pins marking farm and store locations"></div>

<article class="farm-card first">
  <div class="card-bar"><span>Farm Name with Details</span><span>View Foodgallery &gt;&gt;</span></div>
  <div class="card-photo market" role="img" aria-label="Photo of a couple shopping for fresh fruit"></div>
  <div class="card-body">
    <h3>About Us</h3>
    <p>Lorem ipsum dolor sit amet, consectetur adipisicing elit, sed do eiusmod tempor incididunt ut labore et dolore magna aliqua.</p>
    <h3>Our Foods</h3>
    <p>Lorem ipsum dolor sit amet, consectetur adipisicing elit, sed do eiusmod tempor incididunt ut labore et dolore magna aliqua Lorem ipsum dolor sit amet, consectetur adipisicing elit.</p>
  </div>
</article>

<article class="farm-card second">
  <div class="card-bar"><span>Farm Name with Details</span><span>View Foodgallery &gt;&gt;</span></div>
  <div class="card-photo produce" role="img" aria-label="Photo of fresh fruit splashing into water"></div>
  <div class="card-body">
    <h3>About Us</h3>
    <p>Lorem ipsum dolor sit amet, consectetur adipisicing elit, sed do eiusmod tempor incididunt ut labore et dolore magna aliqua.</p>
    <h3>Our Foods</h3>
    <p>Lorem ipsum dolor sit amet, consectetur adipisicing elit, sed do eiusmod tempor incididunt ut labore et dolore magna aliqua Lorem ipsum dolor sit amet, consectetur adipisicing elit.</p>
  </div>
</article>

<div class="more-link">MORE
  <svg width="14" height="11" viewBox="0 0 14 11" aria-hidden="true">
    <path d="M1 1 L7 5 L13 1 M1 5.5 L7 9.5 L13 5.5" fill="none" stroke="#a8620f" stroke-width="2"/>
  </svg>
</div>

<section class="welcome">
  <h1 class="welcome-title"><span class="rule"></span><span><span class="accent">Welcome</span> to our Site</span><span class="rule"></span></h1>
  <p>At Corndell, we will sell from our own farms and will add farmers when we know them and the quality of their products. All products will be absolutely returnable for whatever reason and because we own the entire value chain, we believe our products will be cost competitive orgranic vs. going to the grocery store to buy non-organic of uncertain origin.</p>
  <div class="read-more">More &gt;&gt;</div>
</section>

<footer class="site-footer">
  <div class="legal">Copyright@2013, CORNDELL &nbsp; | &nbsp; Terms &amp; Policy</div>
  <div class="social" aria-label="Social links"><span></span><span></span><span></span></div>
</footer>

</body>
</html>
```